Dr. Marissa Tevlin Medical/Chiropractic Business Card

Dr. Tevlin is a chiropractor and will require a business card that she uses every single day to book appointments on the back side of the card. Currently the office name goes by Dr. Marissa Tevlin. The chiropractic profession is based on the diagnosis and manipulative treatment of misalignments of the joints, especially those of the spinal column, which are held to cause other disorders by affecting the nerves, muscles, and organs. Dr. Marissa Tevlin is looking for a contemporary and minimalistic design.

Industry/Entity Type

Medical

Contact Information for Business Card

Name: Dr. Marissa Tevlin; Address: 748 Harcastle Rd South, London, ON N5R 2K7; Phone Number: 519.274.6193; Fax: 519.281.5046; email: marissa.tevlin@quorvamail.com

Requirements
Must have
• ability to write multiple appointments date/time on the back of card

```html
<!DOCTYPE html>
<html lang="en">
<head>
<meta charset="utf-8">
<title>Dr. Marissa Tevlin – Business Card</title>
<link href="https://fonts.googleapis.com/css2?family=Raleway:wght@400;500;700;800&display=swap" rel="stylesheet">
<style>
  :root {
    --bg-top: #cfe9df;
    --bg-bottom: #acdccf;
    --card: #ffffff;
    --pink: #e6007e;
    --ink: #1c1c1c;
    --shadow: rgba(40, 90, 80, 0.22);
  }
  * { box-sizing: border-box; margin: 0; padding: 0; }
  html, body {
    width: 1200px; height: 856px; overflow: hidden;
    font-family: "Raleway", sans-serif;
  }
  body {
    background: linear-gradient(180deg, var(--bg-top), var(--bg-bottom));
    display: flex; align-items: center; justify-content: center; gap: 44px;
  }
  .card {
    width: 540px; height: 309px;
    background: var(--card);
    border-radius: 26px;
    box-shadow: 0 14px 30px var(--shadow);
    position: relative;
  }

  /* Front */
  .card--front { padding: 40px 44px; color: var(--ink); }
  .card__name { color: var(--pink); font-size: 38px; font-weight: 400; letter-spacing: 0.5px; line-height: 1; }
  .card__title { font-size: 18px; font-weight: 500; margin-top: 6px; }
  .card__address { font-size: 19px; font-weight: 500; line-height: 1.2; margin-top: 20px; margin-left: 24px; }
  .contact-list { list-style: none; margin-top: 18px; margin-left: 40px; }
  .contact-list__item { display: flex; align-items: center; gap: 12px; font-size: 19px; font-weight: 500; height: 30px; }
  .contact-list__icon { width: 24px; height: 24px; flex: none; }

  /* Back */
  .card--back { padding: 26px 40px 20px; color: var(--ink); }
  .appointments__heading { color: var(--pink); font-weight: 800; font-size: 24px; text-align: center; letter-spacing: 1px; }
  .appointments__grid { display: flex; gap: 34px; margin-top: 14px; }
  .appointments__column { flex: 1; display: grid; grid-template-columns: 1.45fr 1fr; column-gap: 14px; row-gap: 0; }
  .appointments__label { font-size: 15px; font-weight: 500; text-align: center; padding-bottom: 2px; }
  .appointments__line { height: 34px; border-bottom: 2px solid var(--pink); }
  .appointments__note { color: var(--pink); font-size: 13px; font-weight: 500; text-align: center; line-height: 1.2; margin-top: 20px; }
</style>
</head>
<body>

<section class="card card--front" aria-label="Business card front">
  <h1 class="card__name">Dr. Marissa Tevlin</h1>
  <p class="card__title">Chiropractor</p>
  <p class="card__address">748 Harcastle Rd South<br>London, ON N5R 2K7</p>
  <ul class="contact-list">
    <li class="contact-list__item">
      <svg class="contact-list__icon" viewBox="0 0 24 24" aria-hidden="true">
        <circle cx="12" cy="12" r="12" fill="var(--pink)"/>
        <path d="M8.2 6.5c.5-.4 1.1-.3 1.4.2l1.1 1.8c.3.5.2 1-.2 1.3l-.8.6c.5 1.3 1.6 2.6 3 3.3l.6-.8c.3-.4.9-.5 1.3-.2l1.8 1.1c.5.3.6.9.2 1.4l-.8.9c-.6.6-1.5.8-2.3.4-2.7-1.2-4.7-3.3-5.8-6-.3-.8-.1-1.7.5-2.3z" fill="#fff"/>
      </svg>
      <span>519.274.6193</span>
    </li>
    <li class="contact-list__item">
      <svg class="contact-list__icon" viewBox="0 0 24 24" aria-hidden="true">
        <circle cx="12" cy="12" r="12" fill="var(--pink)"/>
        <rect x="7" y="6" width="7" height="4" fill="#fff"/>
        <rect x="6" y="10" width="12" height="8" rx="1" fill="#fff"/>
        <rect x="8" y="12" width="2" height="1.5" fill="var(--pink)"/>
        <rect x="11" y="12" width="2" height="1.5" fill="var(--pink)"/>
        <rect x="8" y="14.5" width="2" height="1.5" fill="var(--pink)"/>
        <rect x="11" y="14.5" width="2" height="1.5" fill="var(--pink)"/>
        <rect x="14.5" y="11.5" width="2" height="5" fill="var(--pink)"/>
      </svg>
      <span>Fax: 519.281.5046</span>
    </li>
    <li class="contact-list__item">
      <svg class="contact-list__icon" viewBox="0 0 24 24" aria-hidden="true">
        <circle cx="12" cy="12" r="12" fill="var(--pink)"/>
        <rect x="6" y="8" width="12" height="8.5" fill="#fff"/>
        <path d="M6 8l6 5 6-5" fill="none" stroke="var(--pink)" stroke-width="1.2"/>
      </svg>
      <span>marissa.tevlin@quorvamail.com</span>
    </li>
  </ul>
</section>

<section class="card card--back" aria-label="Business card back">
  <h2 class="appointments__heading">APPOINTMENTS</h2>
  <div class="appointments__grid">
    <div class="appointments__column">
      <span class="appointments__label">Date</span><span class="appointments__label">Time</span>
      <span class="appointments__line"></span><span class="appointments__line"></span>
      <span class="appointments__line"></span><span class="appointments__line"></span>
      <span class="appointments__line"></span><span class="appointments__line"></span>
      <span class="appointments__line"></span><span class="appointments__line"></span>
    </div>
    <div class="appointments__column">
      <span class="appointments__label">Date</span><span class="appointments__label">Time</span>
      <span class="appointments__line"></span><span class="appointments__line"></span>
      <span class="appointments__line"></span><span class="appointments__line"></span>
      <span class="appointments__line"></span><span class="appointments__line"></span>
      <span class="appointments__line"></span><span class="appointments__line"></span>
    </div>
  </div>
  <p class="appointments__note">If you are unable to make your appointment,<br>please call us to reschedule</p>
</section>

</body>
</html>
```